Menu for Coffee Shop / Restaurant

we are looking for someone to redesign our menus. would like something clean and modern, not too over the top. The business is a coffee shop during the day and transitions to a bar/restaurant in the evenings, so we need a design versatile enough to be used on everything from breakfast menus to cocktail menus. i've attached logo files as well as the current menu files. We're looking to do one menu each for breakfast, brunch (served only on weekends), one that combines the items listed on the attached lunch and dinner menus, and a dessert menu.

Industry/Entity Type

Business

Colors

Designer to choose colors to be used in the design.

Requirements
Must have
• 4 menus : breakfast, brunch, regular food service (combine lunch and dinner menus) and a dessert menu
Nice to have
• would prefer that each menu fit on 1 page, not double sided. We're ok with using legal size paper in order to accomodate

```html
<!DOCTYPE html>
<html lang="en">
<head>
<meta charset="utf-8">
<title>Build Your Own Breakfast Sandwich – Breakfast Menu</title>
<link rel="stylesheet" href="https://fonts.googleapis.com/css2?family=Montserrat:wght@500;600;700&family=PT+Serif&display=swap">
<style>
  :root {
    --paper: #ffffff;
    --sky: #4cb9e2;
    --gold: #f4b223;
    --navy: #1d3451;
    --muted: #6e6e6e;
    --rule: #f4b223;
    --heading-font: "Montserrat", sans-serif;
    --body-font: "PT Serif", serif;
  }
  * { box-sizing: border-box; margin: 0; padding: 0; }
  html, body { width: 849px; height: 1200px; overflow: hidden; background: var(--paper); }
  .menu { position: relative; width: 849px; height: 1200px; background: var(--paper); font-family: var(--heading-font); }

  .food { position: absolute; z-index: 0; }
  .food--cheese-board { left: 43px; top: 42px; width: 232px; height: 258px; background: linear-gradient(135deg, #5a3520, #9a6a45 55%, #e8dfc0); }
  .food--cheese-plate { left: 272px; top: 42px; width: 238px; height: 178px; border-radius: 0 0 120px 120px; background: radial-gradient(circle at 45% 50%, #d9c69a 0 30%, #f1efea 31% 100%); }
  .food--salmon-bagel { left: 515px; top: 42px; width: 258px; height: 222px; border-radius: 0 0 40px 90px; background: linear-gradient(160deg, #e9a070, #e46a45 45%, #b9d79a 70%, #f2e2c0); }
  .food--sesame-bagel { left: 740px; top: 42px; width: 66px; height: 154px; border-radius: 60px 0 0 60px; background: linear-gradient(90deg, #c98a4e, #a8692f); }
  .food--cream-dip { left: 521px; top: 278px; width: 135px; height: 134px; border-radius: 50%; background: radial-gradient(circle, #efe4d3 0 55%, #e9eaea 56% 100%); }
  .food--cucumber { left: 774px; top: 265px; width: 32px; height: 80px; border-radius: 40px 0 0 40px; background: linear-gradient(90deg, #cde5b0, #5e9a3e); }
  .food--plain-bagel { left: 712px; top: 345px; width: 94px; height: 195px; border-radius: 100px 0 0 100px; background: linear-gradient(120deg, #f0c48c, #c57a39); }
  .food--avocado { left: 43px; top: 320px; width: 100px; height: 150px; border-radius: 0 80px 80px 0; background: linear-gradient(90deg, #a6c95a, #d8e68a 60%, #8bb243); }
  .food--ciabatta { left: 43px; top: 573px; width: 136px; height: 236px; border-radius: 0 40px 50px 0; background: linear-gradient(140deg, #e2cfb0, #b99a73 60%, #d8c4a2); }
  .food--bacon { left: 692px; top: 563px; width: 114px; height: 202px; border-radius: 40px 0 0 20px; background: linear-gradient(110deg, #8a2a17, #c1532f 50%, #7a2414); }
  .food--tomatoes { left: 735px; top: 820px; width: 71px; height: 146px; border-radius: 50px 0 0 50px; background: radial-gradient(circle at 60% 45%, #e8402e, #b82218); }
  .food--eggs { left: 43px; top: 948px; width: 238px; height: 210px; border-radius: 0 30px 0 0; background: linear-gradient(150deg, #efe5d0, #e6b386 40%, #d99a6a 70%, #eadfca); }
  .food--fried-egg { left: 316px; top: 1068px; width: 180px; height: 90px; border-radius: 90px 90px 0 0; background: radial-gradient(circle at 50% 95%, #f6b120 0 25%, #f8f6f0 26% 100%); }
  .food--skillet-omelet { left: 550px; top: 980px; width: 256px; height: 178px; border-radius: 120px 0 0 0; background: radial-gradient(circle at 60% 70%, #e8b45c 0 45%, #2a2a2a 46% 100%); }

  .title, .builder, .section { z-index: 1; }
  .title { position: absolute; left: 158px; top: 304px; color: var(--sky); font-weight: 600; font-size: 35px; line-height: 36px; letter-spacing: 0; text-transform: uppercase; }

  .builder { position: absolute; width: 290px; }
  .builder--bread { left: 158px; top: 455px; }
  .builder--cheese { left: 466px; top: 455px; }
  .builder--protein { left: 466px; top: 580px; }
  .builder__heading { color: var(--gold); font-weight: 600; font-size: 19px; line-height: 24px; letter-spacing: 3.6px; text-transform: uppercase; }
  .builder__price { color: var(--gold); font-weight: 500; font-size: 14px; line-height: 16px; letter-spacing: 3px; margin-bottom: 4px; }
  .builder__list { list-style: none; }
  .builder__list li { color: var(--navy); font-weight: 700; font-size: 11px; line-height: 12.2px; text-transform: uppercase; }
  .builder__list li::before { content: "• "; }

  .section { position: absolute; top: 752px; }
  .section--sandwiches { left: 158px; width: 215px; }
  .section--omelets { left: 464px; width: 214px; }
  .section__heading { color: var(--gold); font-weight: 600; font-size: 18px; letter-spacing: 3.6px; text-transform: uppercase; text-align: center; padding-bottom: 8px; border-bottom: 1.5px solid var(--rule); }
  .section--sandwiches .section__heading { margin-left: 29px; width: 196px; }
  .section--omelets .section__heading { width: 226px; }
  .dish-list { margin-top: 29px; }
  .dish { margin-bottom: 8px; }
  .dish__row { display: flex; justify-content: space-between; color: var(--navy); font-weight: 700; font-size: 11px; line-height: 13px; text-transform: uppercase; }
  .dish__row .dish__price { font-weight: 600; }
  .dish__desc { color: var(--muted); font-family: var(--body-font); font-size: 8.6px; line-height: 9.6px; padding-left: 9px; width: 190px; }
  .dish__desc--wide { width: 222px; }
</style>
</head>
<body>
<main class="menu">
  <div class="food food--cheese-board" role="img" aria-label="Cheese and cured sausage on a wooden board"></div>
  <div class="food food--cheese-plate" role="img" aria-label="Wedge of aged cheese with prosciutto on a white plate"></div>
  <div class="food food--salmon-bagel" role="img" aria-label="Bagel with smoked salmon, cucumber and red onion"></div>
  <div class="food food--sesame-bagel" role="img" aria-label="Sesame bagel"></div>
  <div class="food food--cream-dip" role="img" aria-label="Glass bowl of mayonnaise"></div>
  <div class="food food--cucumber" role="img" aria-label="Cucumber slices"></div>
  <div class="food food--plain-bagel" role="img" aria-label="Plain bagel"></div>
  <div class="food food--avocado" role="img" aria-label="Sliced avocado fan"></div>
  <div class="food food--ciabatta" role="img" aria-label="Ciabatta roll"></div>
  <div class="food food--bacon" role="img" aria-label="Crispy bacon strips"></div>
  <div class="food food--tomatoes" role="img" aria-label="Cherry tomatoes on the vine"></div>
  <div class="food food--eggs" role="img" aria-label="Brown eggs in a carton"></div>
  <div class="food food--fried-egg" role="img" aria-label="Fried egg sunny side up"></div>
  <div class="food food--skillet-omelet" role="img" aria-label="Omelet in a cast iron skillet"></div>

  <h1 class="title">Build Your<br>Own Breakfast<br>Sandwich</h1>

  <section class="builder builder--bread">
    <h2 class="builder__heading">Choose Your<br>Bread</h2>
    <p class="builder__price">2.25</p>
    <ul class="builder__list">
      <li>Bagels (Daily Selection)</li>
      <li>Brioche Roll</li>
      <li>Brioche Toast</li>
      <li>Ciabatta Rolls</li>
      <li>Croissant (Add $1.00)</li>
      <li>Gluten Free Bagel (Add $1.00)</li>
    </ul>
  </section>

  <section class="builder builder--cheese">
    <h2 class="builder__heading">Add Cheese</h2>
    <p class="builder__price">1.00</p>
    <ul class="builder__list">
      <li>American</li>
      <li>Cheddar</li>
      <li>Pepper Jack</li>
      <li>Swiss</li>
      <li>Cream Cheese</li>
      <li>Flavor Cream Cheese (Add $.50)</li>
    </ul>
  </section>

  <section class="builder builder--protein">
    <h2 class="builder__heading">Add Protein</h2>
    <p class="builder__price">1.00</p>
    <ul class="builder__list">
      <li>Bacon</li>
      <li>Egg</li>
      <li>Turkey Bacon</li>
      <li>Pork Roll</li>
      <li>Sausage</li>
      <li>Avocado</li>
    </ul>
  </section>

  <section class="section section--sandwiches">
    <h2 class="section__heading">Sandwiches</h2>
    <div class="dish-list">
      <div class="dish">
        <div class="dish__row"><span>EBLT</span><span class="dish__price">7.95</span></div>
        <p class="dish__desc">Fried egg, crispy bacon, arugula, tomato, and mayonnaise on brioche roll</p>
      </div>
      <div class="dish">
        <div class="dish__row"><span>Smoked Salmon Sandwich</span><span class="dish__price">11.95</span></div>
        <p class="dish__desc">Sliced smoked salmon, cream cheese, red onion, lettuce, and tomato between a soft toasted brioche roll</p>
      </div>
      <div class="dish">
        <div class="dish__row"><span>Breakfast Burger</span><span class="dish__price">13.95</span></div>
        <p class="dish__desc">Angus Beef, sausage patty, cheddar cheese, caramelized onions, lettuce and tomato on toasted brioche roll</p>
      </div>
    </div>
  </section>

  <section class="section section--omelets">
    <h2 class="section__heading">Omelets</h2>
    <div class="dish-list">
      <div class="dish">
        <div class="dish__row"><span>Egg White Omelet</span><span class="dish__price">9.95</span></div>
        <p class="dish__desc dish__desc--wide">marinated chicken breast and broccoli stuffed</p>
      </div>
      <div class="dish">
        <div class="dish__row"><span>Vegetable Omelet</span><span class="dish__price">9.95</span></div>
        <p class="dish__desc">Mushrooms, peppers, red onion, spinach, and cheddar cheese</p>
      </div>
      <div class="dish">
        <div class="dish__row"><span>Chicken Omelet</span><span class="dish__price">9.95</span></div>
        <p class="dish__desc">Marinated chicken breast, spinach, tomato, caramelized onions, and pepper jack cheese</p>
      </div>
      <div class="dish">
        <div class="dish__row"><span>Smoked Salmon Omelet</span><span class="dish__price">11.95</span></div>
        <p class="dish__desc dish__desc--wide">Green onions, red peppers, cream cheese, and sliced smoked salmon stuffed inside an omelet</p>
      </div>
    </div>
  </section>
</main>
</body>
</html>
```